Electronic Time-sheet for phones

I need a time-sheet that can be accessed on the phone, be completed, then have the ability to electronically sign. The time sheet needs to be used two fold for supervision to verify hours and quantities and also for the client to be able to electronically sign. The time-sheet should be daily or weekly if we can get the data to fit. We are trying to streamline field supervisors having to log on to a computer to access a server just to do time-sheets. We need it to be user friendly. We need to have two places to have electronic signatures. One for supervisor or authorized representative and the other for the client to sign.

Target Market(s)

Industrial clients

Industry/Entity Type

Oil And Gas

Requirements
Must have
• hours, quantities, project name, location, signature line etc
Nice to have
• n/a
Should not have
• n/a

```html
<!DOCTYPE html>
<html lang="en">
<head>
<meta charset="utf-8">
<title>Daily Time-sheet</title>
<link href="https://fonts.googleapis.com/css2?family=Roboto:wght@300;400;500;700;900&display=swap" rel="stylesheet">
<style>
  :root {
    --header-top: #152f62;
    --header-bottom: #10275a;
    --meta-bar: #030811;
    --page: #08142b;
    --page-deep: #050d1f;
    --line: #2a3954;
    --text: #e8ecf3;
    --muted: #9aa3b3;
    --accent: #eef18c;
    --head-col: #dedcae;
    --chat-green: #8fd46a;
    --chat-blue: #7d9fd6;
  }
  * { box-sizing: border-box; margin: 0; padding: 0; }
  html, body { width: 1200px; height: 2271px; overflow: hidden; }
  body {
    position: relative;
    background: linear-gradient(180deg, var(--page) 0%, var(--page-deep) 100%);
    font-family: "Roboto", sans-serif;
    color: var(--text);
  }
  .app-header {
    position: absolute; left: 0; top: 0; width: 1200px; height: 310px;
    background: linear-gradient(180deg, var(--header-top), var(--header-bottom));
  }
  .menu-toggle { position: absolute; left: 124px; top: 131px; }
  .brand {
    position: absolute; left: 0; width: 1200px; top: 108px;
    text-align: center; font-weight: 900; font-size: 66px; letter-spacing: 2px; color: #ffffff;
  }
  .login { position: absolute; left: 926px; top: 106px; display: flex; align-items: center; gap: 14px; font-size: 20px; letter-spacing: 1px; }
  .header-rule { position: absolute; left: 129px; top: 215px; width: 923px; height: 1px; background: #4a6390; }
  .client-name { position: absolute; left: 0; width: 1200px; top: 230px; text-align: center; font-size: 24px; letter-spacing: 2px; }
  .project-site { position: absolute; left: 0; width: 1200px; top: 268px; text-align: center; font-size: 18px; letter-spacing: 2.5px; color: var(--accent); }

  .meta-bar {
    position: absolute; left: 0; top: 310px; width: 1200px; height: 92px;
    background: var(--meta-bar); border-bottom: 1px solid var(--line);
    font-size: 20px;
  }
  .meta-item { position: absolute; top: 0; height: 92px; display: flex; align-items: center; }
  .meta-label { letter-spacing: 2px; color: #b9c1cf; margin-right: 14px; }
  .meta-value { color: #ffffff; }
  .foreman { left: 100px; }
  .approved { left: 475px; }
  .signature-area { width: 120px; height: 44px; background: linear-gradient(90deg, rgba(255,255,255,0.18), rgba(255,255,255,0.06)); border-radius: 22px; }
  .date { left: 890px; }

  .field-label { position: absolute; left: 123px; font-size: 20px; letter-spacing: 1.2px; }
  .label-description { top: 449px; }
  .label-cost { top: 726px; }
  .description-box { position: absolute; left: 123px; top: 495px; width: 932px; height: 164px; border: 1px solid var(--line); }
  .cost-line { position: absolute; left: 123px; top: 808px; width: 932px; height: 1px; background: var(--line); }

  .hours-card { position: absolute; left: 53px; top: 888px; width: 1103px; height: 1069px; border: 1px solid var(--line); background: rgba(4,10,24,0.5); }
  .crew-table { position: absolute; left: 17px; top: 0; width: 1072px; border-collapse: collapse; }
  .crew-table th {
    height: 84px; text-align: left; font-weight: 500; font-size: 20px; letter-spacing: 1.5px;
    color: var(--head-col); border-bottom: 1px solid var(--line); padding-top: 4px;
  }
  .crew-table td { height: 54.2px; font-size: 20px; color: var(--muted); font-weight: 400; }
  .crew-table tbody tr:first-child td { padding-top: 20px; height: 74px; }
  .col-name { padding-left: 53px; width: 236px; }
  .col-class { width: 300px; }
  .col-emp { width: 196px; }
  .col-hours { width: 176px; }
  .totals-rule { position: absolute; left: 17px; top: 886px; width: 1072px; height: 1px; background: var(--line); }
  .totals-row { position: absolute; left: 98px; font-size: 30px; letter-spacing: 1px; width: 1000px; }
  .totals-row span { position: absolute; top: 0; color: var(--accent); }
  .totals-row .t-hours { left: 695px; }
  .totals-row .t-total { left: 850px; }
  .row-hours { top: 928px; }
  .row-qty { top: 989px; }

  .comments-button {
    position: absolute; left: 488px; top: 1923px; width: 222px; height: 222px; border-radius: 50%;
    background: #0f2444; display: flex; align-items: center; justify-content: center;
    box-shadow: 0 10px 30px rgba(0,0,0,0.6);
  }
  .comments-inner {
    width: 198px; height: 198px; border-radius: 50%; background: #ffffff;
    display: flex; flex-direction: column; align-items: center; justify-content: center; gap: 4px;
  }
  .comments-label { font-size: 22px; color: #333b47; letter-spacing: 1px; }
</style>
</head>
<body>
  <header class="app-header">
    <svg class="menu-toggle" width="50" height="36" viewBox="0 0 50 36">
      <rect x="0" y="0" width="50" height="4" fill="#fff"/>
      <rect x="0" y="16" width="36" height="4" fill="#fff"/>
      <rect x="0" y="32" width="50" height="4" fill="#fff"/>
    </svg>
    <div class="brand">VERTEX</div>
    <div class="login">
      <svg width="52" height="52" viewBox="0 0 52 52">
        <circle cx="26" cy="26" r="24" fill="none" stroke="#fff" stroke-width="2.5"/>
        <circle cx="26" cy="20" r="8" fill="none" stroke="#fff" stroke-width="2.5"/>
        <path d="M11 42 C14 32 38 32 41 42" fill="none" stroke="#fff" stroke-width="2.5"/>
      </svg>
      <span>Login</span>
    </div>
    <div class="header-rule"></div>
    <div class="client-name">NORTHFIELD CHEMICAL, INC.</div>
    <div class="project-site">NEW UNIT#1, CANADA</div>
  </header>

  <section class="meta-bar">
    <div class="meta-item foreman"><span class="meta-label">FOREMAN :</span><span class="meta-value">Owen Tate</span></div>
    <div class="meta-item approved"><span class="meta-label">APPROVED BY :</span><div class="signature-area" role="img" aria-label="Approver signature"></div></div>
    <div class="meta-item date"><span class="meta-label">DATE:</span><span class="meta-value">11-08-2018</span></div>
  </section>

  <div class="field-label label-description">DESCRIPTION OF WORK PERFORMED</div>
  <div class="description-box"></div>
  <div class="field-label label-cost">COST / PHASE CODE</div>
  <div class="cost-line"></div>

  <section class="hours-card">
    <table class="crew-table">
      <thead>
        <tr><th class="col-name">NAME</th><th class="col-class">CLASS</th><th class="col-emp">EMP NO.</th><th class="col-hours">HOURS</th><th>TOTAL</th></tr>
      </thead>
      <tbody>
        <tr><td class="col-name">Liam</td><td>Daily Quantities</td><td>1547</td><td>5</td><td>15</td></tr>
        <tr><td class="col-name">Lucas</td><td>Daily Quantities</td><td>1234</td><td>10</td><td>30</td></tr>
        <tr><td class="col-name">Elizabeth</td><td>Daily Quantities</td><td>1537</td><td>8</td><td>24</td></tr>
        <tr><td class="col-name">Michael</td><td>Daily Quantities</td><td>2323</td><td>12</td><td>36</td></tr>
        <tr><td class="col-name">Liam</td><td>Daily Quantities</td><td>1867</td><td>15</td><td>45</td></tr>
        <tr><td class="col-name">Lucas</td><td>Daily Quantities</td><td>1436</td><td>7</td><td>21</td></tr>
        <tr><td class="col-name">Elizabeth</td><td>Daily Quantities</td><td>2130</td><td>6</td><td>20</td></tr>
        <tr><td class="col-name">Michael</td><td>Daily Quantities</td><td>1865</td><td>15</td><td>45</td></tr>
        <tr><td class="col-name">Liam</td><td>Daily Quantities</td><td>2103</td><td>7</td><td>21</td></tr>
        <tr><td class="col-name">Lucas</td><td>Daily Quantities</td><td>1754</td><td>12</td><td>36</td></tr>
        <tr><td class="col-name">Elizabeth</td><td>Daily Quantities</td><td>1248</td><td>11</td><td>33</td></tr>
        <tr><td class="col-name">Michael</td><td>Daily Quantities</td><td>1537</td><td>10</td><td>30</td></tr>
        <tr><td class="col-name">Liam</td><td>Daily Quantities</td><td>1836</td><td>9</td><td>21</td></tr>
        <tr><td class="col-name">Lucas</td><td>Daily Quantities</td><td>2013</td><td>4</td><td>12</td></tr>
      </tbody>
    </table>
    <div class="totals-rule"></div>
    <div class="totals-row row-hours">HOUR TOTALS<span class="t-hours">134</span><span class="t-total">768</span></div>
    <div class="totals-row row-qty">QUANTITY TOTALS<span class="t-hours">100</span><span class="t-total">768</span></div>
  </section>

  <div class="comments-button">
    <div class="comments-inner">
      <svg width="104" height="90" viewBox="0 0 104 90">
        <rect x="26" y="0" width="78" height="62" fill="var(--chat-blue)"/>
        <path d="M0 22 H76 V74 H20 L6 88 V74 H0 Z" fill="var(--chat-green)"/>
        <circle cx="22" cy="48" r="4" fill="#fff"/>
        <circle cx="38" cy="48" r="4" fill="#fff"/>
        <circle cx="54" cy="48" r="4" fill="#fff"/>
      </svg>
      <span class="comments-label">Comments</span>
    </div>
  </div>
</body>
</html>
```